Fresh Dwelling Tract Hub needs a new Landing Page

I like to get a landing page or website with 2-3 pages to help target home buyers who are looking to buy homes from builders such as TQ Estates, Vostrum, P.J. Calloway, etc. The landing page/website to be non-cluttered and be able to explain to home buyers that there are many benefits to include me as their buyer's agent when they buy a brand new home from any builders.
I may want to incorporate a short explanation video (animated) on the landing page and then for the viewer to click on a button that will take them to another page where they can search for new homes from different builders.
Target Market(s)
Home buyers looking to buy brand new home from builders such as TQ Estates, Vostrum, P.J. Calloway, etc.
Industry/Entity Type
Real Estate
Number of Pages Required
2 page
Requirements
Must have
- The landing page may have the explanation video at the bottom of the landing page (scrolled down) or there may be a CALL TO ACTION button that takes the viewer to the 2nd page to watch the explanation video. Once they watched the explanation video and are still interested, they can click on another CALL TO ACTION button that will take them to another website that they will be able to search for all the available new homes and register their contact information.
Should not have
- No clutters and no dark colors.

```html
<!DOCTYPE html>
<html lang="en">
<head>
<meta charset="utf-8">
<title>Fresh Dwelling Tract Hub – Search for New Homes</title>
<link rel="stylesheet" href="https://fonts.googleapis.com/css2?family=Oswald:wght@500&family=Open+Sans:wght@400&family=Roboto:wght@500&family=Dancing+Script:wght@500&display=swap">
<style>
  :root {
    --headline-blue: #2a5196;
    --accent-green: #b9c143;
    --accent-green-edge: #cfd12a;
    --text-dark: #1e1e1e;
    --icon-grey: #4a4a4a;
    --footer-bg: rgba(18, 18, 18, 0.93);
    --footer-text: #ffffff;
    --brand-brown: #4a3522;
  }
  * { box-sizing: border-box; margin: 0; padding: 0; }
  html, body { width: 1200px; height: 724px; overflow: hidden; }
  body { position: relative; font-family: "Open Sans", sans-serif; color: var(--text-dark); background: #f2f2f2; }

  .hero-photo {
    position: absolute; inset: 0;
    background:
      linear-gradient(180deg, rgba(255,255,255,0) 0%, rgba(255,255,255,0) 55%, rgba(200,200,198,0.55) 78%, rgba(140,140,135,0.6) 100%),
      linear-gradient(90deg, #dcdcdc 0%, #f4f4f4 12%, #fafafa 50%, #f2f2f2 88%, #e2e2e2 100%);
  }
  .hero-photo::after {
    content: ""; position: absolute; left: 140px; right: 80px; top: 420px; height: 210px;
    background: linear-gradient(90deg, rgba(210,208,204,0.7) 0%, rgba(60,110,90,0.35) 38%, rgba(200,195,185,0.4) 58%, rgba(110,120,70,0.45) 85%, rgba(90,150,70,0.4) 100%);
    border-radius: 30px; filter: blur(18px);
  }

  .site-header { position: absolute; top: 0; left: 0; right: 0; height: 120px; }
  .brand { position: absolute; left: 88px; top: 58px; display: flex; align-items: center; gap: 8px; }
  .brand-mark { width: 12px; height: 12px; border-radius: 50%; background: var(--accent-green); }
  .brand-name { font-family: "Open Sans", sans-serif; font-size: 15px; color: var(--brand-brown); letter-spacing: 0.5px; }

  .menu-toggle { position: absolute; left: 896px; top: 55px; width: 22px; height: 18px; }
  .menu-toggle span { display: block; height: 3px; background: var(--icon-grey); border-radius: 1px; margin-bottom: 4.5px; }
  .phone { position: absolute; left: 946px; top: 48px; display: flex; align-items: center; gap: 6px; font-size: 20px; color: var(--text-dark); }
  .phone-icon { width: 18px; height: 18px; border-radius: 3px; background: var(--accent-green); display: flex; align-items: center; justify-content: center; }

  .hero-content { position: absolute; left: 0; right: 0; top: 180px; text-align: center; }
  .hero-title { font-family: "Oswald", sans-serif; font-weight: 500; font-size: 61px; line-height: 72px; color: var(--headline-blue); letter-spacing: -0.5px; }
  .hero-lead { margin-top: 20px; font-size: 21px; line-height: 33px; color: var(--text-dark); }
  .cta-button {
    display: inline-block; margin-top: 20px; width: 284px; height: 53px; line-height: 51px;
    border-radius: 27px; background: var(--accent-green); border: 1px solid var(--accent-green-edge);
    font-family: "Roboto", sans-serif; font-weight: 500; font-size: 19.5px; color: #fff; text-decoration: none;
    box-shadow: 0 6px 14px rgba(0,0,0,0.18);
  }

  .slide-dots { position: absolute; left: 1140px; top: 280px; }

  .site-footer { position: absolute; left: 0; right: 0; bottom: 0; height: 89px; background: var(--footer-bg); color: var(--footer-text); }
  .copyright { position: absolute; left: 104px; top: 38px; font-size: 17.5px; }
  .social-links { position: absolute; left: 904px; top: 36px; display: flex; gap: 8px; }
  .social-links a { width: 26px; height: 26px; border: 1.5px solid #fff; border-radius: 50%; display: flex; align-items: center; justify-content: center; }
</style>
</head>
<body>
  <div class="hero-photo" role="img" aria-label="Bright white living room with a light wooden sofa, green throw, coffee table, olive armchair and potted fern"></div>

  <header class="site-header">
    <a class="brand" href="#"><span class="brand-mark"></span><span class="brand-name">Fresh Dwelling Tract Hub</span></a>
    <div class="menu-toggle" aria-label="Menu"><span></span><span></span><span></span></div>
    <div class="phone">
      <span class="phone-icon">
        <svg width="12" height="12" viewBox="0 0 24 24"><path fill="#fff" d="M6.6 10.8a15.1 15.1 0 0 0 6.6 6.6l2.2-2.2a1 1 0 0 1 1-.25 11.4 11.4 0 0 0 3.6.57 1 1 0 0 1 1 1V20a1 1 0 0 1-1 1A17 17 0 0 1 3 4a1 1 0 0 1 1-1h3.5a1 1 0 0 1 1 1c0 1.25.2 2.45.57 3.6a1 1 0 0 1-.25 1z"/></svg>
      </span>
      <span>: 555 308 4127</span>
    </div>
  </header>

  <main class="hero-content">
    <h1 class="hero-title">SEARCH FOR NEW HOMES</h1>
    <p class="hero-lead">It is a long established fact that a reader will be distracted by the<br>readable content of a page when looking at its layout</p>
    <a class="cta-button" href="#">Search For New Homes</a>
  </main>

  <svg class="slide-dots" width="30" height="80" viewBox="0 0 30 80" aria-hidden="true">
    <line x1="12" y1="8" x2="22" y2="25" stroke="#fff" stroke-width="1"/>
    <circle cx="12" cy="8" r="4.5" fill="var(--accent-green)"/>
    <circle cx="22" cy="25" r="4.5" fill="#fff"/>
    <circle cx="22" cy="42" r="4.5" fill="#fff"/>
    <circle cx="22" cy="59" r="4.5" fill="#fff"/>
    <circle cx="22" cy="76" r="4.5" fill="#fff"/>
  </svg>

  <footer class="site-footer">
    <p class="copyright">Copyright © 2018. All Rights Reserved</p>
    <nav class="social-links" aria-label="Social links">
      <a href="#" aria-label="Network one"></a>
      <a href="#" aria-label="Network two"></a>
      <a href="#" aria-label="Network three"></a>
      <a href="#" aria-label="Network four"></a>
      <a href="#" aria-label="Network five"></a>
      <a href="#" aria-label="Email">
        <svg width="12" height="9" viewBox="0 0 12 9"><rect x="0.5" y="0.5" width="11" height="8" rx="1" fill="none" stroke="#fff"/><path d="M1 1l5 4 5-4" fill="none" stroke="#fff"/></svg>
      </a>
    </nav>
  </footer>
</body>
</html>
```